I need a business card.

I need a simple, minimalist, business card. I think the coolest business card I have ever seen is Marty Vexler's from Kestrel's 9... it is just a little creepy for the real world.
I am a photographer and I need a card that I can give to brides or potential portrait customers that is simple and classy.
My name is Glen Hardesty. My website is www.glenhardesty-example.com
Please design my card.
I think it could be as simple as my name, phone # and website... where the rest of my contact could be found... or maybe my email and no website... I am open to ideas. I imagined the card on thick card stock with a black background...

```html
<!DOCTYPE html>
<html lang="en">
<head>
<meta charset="utf-8">
<title>Glen Hardesty Photography — Business Card</title>
<link href="https://fonts.googleapis.com/css2?family=Arimo:wght@700&display=swap" rel="stylesheet">
<style>
  :root {
    --backdrop: #adadad;
    --card-light: #232323;
    --card-mid: #111111;
    --card-dark: #000000;
    --ink: #ffffff;
  }
  * { margin: 0; padding: 0; box-sizing: border-box; }
  html, body {
    width: 1200px;
    height: 1200px;
    overflow: hidden;
    background: var(--backdrop);
  }
  .canvas {
    position: relative;
    width: 1200px;
    height: 1200px;
  }
  .card {
    position: absolute;
    left: 70px;
    top: 274px;
    width: 1064px;
    height: 650px;
    background: radial-gradient(ellipse 70% 80% at 38% 45%, var(--card-light) 0%, var(--card-mid) 55%, var(--card-dark) 100%);
    color: var(--ink);
    font-family: "Arimo", Arial, Helvetica, sans-serif;
    font-weight: 700;
  }
  .identity {
    position: absolute;
    left: 96px;
    top: 248px;
    display: flex;
    flex-direction: column;
    align-items: flex-end;
  }
  .identity__name {
    font-size: 84px;
    line-height: 1;
    letter-spacing: 0.1em;
    text-transform: uppercase;
    white-space: nowrap;
  }
  .identity__trade {
    margin-top: 10px;
    margin-right: 6px;
    font-size: 29px;
    line-height: 1;
    letter-spacing: 0.12em;
    text-transform: uppercase;
  }
  .contact {
    position: absolute;
    left: 306px;
    top: 438px;
    font-size: 30px;
    line-height: 40px;
    letter-spacing: 0.08em;
    white-space: nowrap;
  }
</style>
</head>
<body>
  <div class="canvas">
    <section class="card">
      <div class="identity">
        <h1 class="identity__name">Glen Hardesty</h1>
        <p class="identity__trade">Photography</p>
      </div>
      <div class="contact">
        <p class="contact__web">www.glenhardesty-example.com</p>
        <p class="contact__phone">phone number here</p>
      </div>
    </section>
  </div>
</body>
</html>
```